Children's martial arts flyer for new classes

Need a postcard flyer addressing the attached spec (see file).

Flyer needs to be Postcard Size and be suited in style to the target demographic which is parents of children aged 5-12 years old.

Classes are new.

Postcard must include the logo and a picture. I have included an example pic in the attached file, but feel free to use other suitable pics.

Target Market(s)

Parents with children aged 5-12 years old

Colors

Designer to choose colors to be used in the design.

Requirements
Must have
• clean look.
• professional.

```html
<!DOCTYPE html>
<html lang="en">
<head>
<meta charset="utf-8">
<title>Children's martial art classes</title>
<link rel="stylesheet" href="https://fonts.googleapis.com/css2?family=Oswald:wght@400;500&display=swap">
<style>
  :root {
    --ink: #111111;
    --accent: #e8502a;
    --orange-top: #f4a12c;
    --orange-mid: #ef6f2c;
    --red-base: #e42b30;
    --paper: #ffffff;
    --photo-light: #f1ede7;
    --photo-warm: #e3d9cc;
    --map-tone: #e9e5de;
  }
  html, body {
    margin: 0;
    padding: 0;
    overflow: hidden;
    background: var(--paper);
  }
  .flyer {
    position: relative;
    width: 1200px;
    height: 786px;
    overflow: hidden;
    background: var(--paper);
    font-family: "Oswald", sans-serif;
  }
  .wave-band {
    position: absolute;
    left: 0;
    top: 0;
    width: 1200px;
    height: 786px;
  }
  .headline {
    position: absolute;
    top: 3px;
    left: 0;
    width: 1200px;
    margin: 0;
    text-align: center;
    font-weight: 500;
    font-size: 68px;
    line-height: 1;
    color: var(--ink);
    letter-spacing: -0.5px;
  }
  .tagline {
    position: absolute;
    top: 80px;
    left: 0;
    width: 1200px;
    margin: 0;
    text-align: center;
    font-weight: 400;
    font-size: 38px;
    line-height: 38px;
    color: var(--accent);
  }
  .rule-top {
    position: absolute;
    left: 0;
    top: 207px;
    width: 1200px;
    height: 7px;
    background: var(--ink);
  }
  .kicker-art {
    position: absolute;
    top: 2px;
    width: 184px;
    height: 202px;
    border-radius: 40px 40px 6px 6px;
    background: var(--ink);
  }
  .kicker-art.left { left: 24px; }
  .kicker-art.right { left: 992px; }
  .photo {
    position: absolute;
    border-radius: 30px;
    background: linear-gradient(160deg, var(--photo-light), var(--photo-warm));
  }
  .photo.seated { left: 64px; top: 182px; width: 340px; height: 234px; }
  .photo.kicking { left: 750px; top: 164px; width: 142px; height: 300px; }
  .photo.standing { left: 916px; top: 112px; width: 148px; height: 330px; }
  .brand {
    position: absolute;
    left: 455px;
    top: 408px;
    width: 270px;
    display: flex;
    align-items: center;
    justify-content: center;
    gap: 10px;
    font-weight: 500;
    font-size: 28px;
    line-height: 1;
    color: var(--ink);
    white-space: nowrap;
  }
  .brand-dot {
    width: 16px;
    height: 16px;
    border-radius: 50%;
    background: var(--ink);
    flex: none;
  }
  .call {
    position: absolute;
    left: 70px;
    top: 574px;
    margin: 0;
    color: var(--paper);
    font-weight: 400;
    line-height: 1;
    white-space: nowrap;
  }
  .call-lead {
    font-size: 50px;
    line-height: 1;
    margin-right: 10px;
  }
  .call-number {
    font-size: 78px;
    line-height: 1;
    font-weight: 500;
    letter-spacing: -1px;
  }
  .call-line {
    position: absolute;
    left: 82px;
    top: 656px;
    margin: 0;
    color: var(--paper);
    font-size: 52px;
    line-height: 1;
    font-weight: 400;
    white-space: nowrap;
  }
  .map-area {
    position: absolute;
    left: 790px;
    top: 516px;
    width: 356px;
    height: 198px;
    border-radius: 8px;
    background: var(--map-tone);
  }
  .address {
    position: absolute;
    right: 54px;
    top: 723px;
    margin: 0;
    color: var(--paper);
    font-size: 24.5px;
    line-height: 1;
    font-weight: 400;
    white-space: nowrap;
  }
  .rule-bottom {
    position: absolute;
    left: 0;
    top: 754px;
    width: 1200px;
    height: 10px;
    background: var(--ink);
  }
  .base-band {
    position: absolute;
    left: 0;
    top: 766px;
    width: 1200px;
    height: 20px;
    background: var(--red-base);
  }
</style>
</head>
<body>
<main class="flyer">
  <svg class="wave-band" viewBox="0 0 1200 786" aria-hidden="true">
    <defs>
      <linearGradient id="band-fill" x1="0" y1="0" x2="0" y2="1">
        <stop offset="0" stop-color="#f4a12c"/>
        <stop offset="0.5" stop-color="#ef6f2c"/>
        <stop offset="1" stop-color="#e42b30"/>
      </linearGradient>
    </defs>
    <path d="M0 438 C 110 410, 200 396, 300 402 C 430 410, 560 480, 720 478 C 880 476, 1040 420, 1200 344 L 1200 756 L 0 756 Z" fill="url(#band-fill)"/>
  </svg>

  <div class="kicker-art left" role="img" aria-label="Black silhouette of a martial artist performing a high kick"></div>
  <div class="kicker-art right" role="img" aria-label="Black silhouette of a martial artist performing a high kick"></div>

  <h1 class="headline">Children’s martial art classes</h1>
  <p class="tagline">Fun and exciting yet controlled and disciplined<br>Tuesday’s and Thursday’s<br>6pm</p>

  <div class="rule-top"></div>

  <div class="photo seated" role="img" aria-label="Photo of a smiling young girl in a white uniform sitting and stretching"></div>
  <div class="photo kicking" role="img" aria-label="Photo of a boy in a white uniform doing a front kick"></div>
  <div class="photo standing" role="img" aria-label="Photo of a smiling girl in a white uniform with a yellow belt"></div>

  <div class="brand"><span class="brand-dot"></span>Rising Kick Academy</div>

  <p class="call"><span class="call-lead">Call</span><span class="call-number">0400 555 218</span></p>
  <p class="call-line">to book a free trial class</p>

  <div class="map-area" role="img" aria-label="Street map showing the class location"></div>
  <p class="address">4/18 Harlow Street Brookvale VIC 3099</p>

  <div class="rule-bottom"></div>
  <div class="base-band"></div>
</main>
</body>
</html>
```